looking for sleek business card to standout from the crowd!

We are a young biotechnology company looking to help you personalize your health through understanding your genetic make up. We need you help in making a clean but sleek business card design using our new logo. The goal? Any time we give our cards out, people say "nice card!" The feel we are going for is "modern-techy". We don't want to come across as an old, giant pharma company, but not trying to be a hipster either.

Target Market(s)

healthcare and biotechnology industry.

Industry/Entity Type

Biotechnology

Contact Information for Business Card

Info to include on the card will be NAME, TITLE, EMAIL, PHONE. The companies website (www.corvalinbio.com) should also be on the card some where. Would like the logo, when printed, to be raised.

Requirements
Must have
• The logo we have attached in the color it is in. Fonts for text should lean toward more professional/tech.
Nice to have
• Prefer white/light color background
Should not have
• cartoons, landscape backgrounds images.

```html
<!DOCTYPE html>
<html lang="en">
<head>
<meta charset="utf-8">
<title>Corvalin Business Card</title>
<link rel="stylesheet" href="https://fonts.googleapis.com/css2?family=Lato:wght@300;400;700&display=swap">
<style>
  :root {
    --page-bg: #e9e7e3;
    --card-light: #f4f4f4;
    --card-light-2: #e6e6e6;
    --card-dark: #29292c;
    --brand-blue: #1b78c2;
    --brand-blue-deep: #1566a8;
    --accent-green: #8cc63f;
    --text-light: #e8e8e8;
    --text-muted: #b9b9bd;
    --shadow: rgba(0, 0, 0, 0.22);
  }
  * { box-sizing: border-box; margin: 0; padding: 0; }
  html, body {
    width: 1200px;
    height: 902px;
    overflow: hidden;
    background: var(--page-bg);
    font-family: "Lato", Arial, sans-serif;
  }
  .sheet { position: relative; width: 1200px; height: 902px; }
  .card {
    position: absolute;
    left: 260px;
    width: 680px;
    height: 390px;
    overflow: hidden;
    box-shadow: 0 10px 28px var(--shadow);
  }
  .card--front { top: 40px; }
  .card--back { top: 472px; background: var(--card-dark); }

  /* front */
  .front-pattern {
    position: absolute;
    inset: 0;
    background: radial-gradient(circle at 45% 55%, var(--card-light) 0%, var(--card-light-2) 100%);
  }
  .brand-name {
    position: absolute;
    left: 50%;
    top: 50%;
    transform: translate(-50%, -50%);
    font-weight: 700;
    font-size: 64px;
    letter-spacing: 6px;
    color: var(--card-dark);
    white-space: nowrap;
  }

  /* back */
  .title-band {
    position: absolute;
    left: 0;
    top: 40px;
    width: 100%;
    height: 70px;
    background: linear-gradient(90deg, var(--brand-blue-deep), var(--brand-blue));
  }
  .title-band__label {
    position: absolute;
    left: 300px;
    top: 13px;
    font-weight: 300;
    font-size: 30px;
    color: #fff;
    letter-spacing: 0.5px;
  }
  .title-band__rule {
    position: absolute;
    left: 306px;
    top: 56px;
    width: 150px;
    height: 2px;
    background: #fff;
  }
  .side-tab {
    position: absolute;
    left: 0;
    top: 150px;
    width: 40px;
    height: 120px;
    background: var(--brand-blue);
  }
  .person {
    position: absolute;
    left: 300px;
    top: 134px;
  }
  .person__name {
    font-weight: 700;
    font-size: 24px;
    color: #fff;
    letter-spacing: 0.4px;
  }
  .person__title {
    margin-top: 4px;
    font-weight: 300;
    font-size: 17px;
    color: var(--text-muted);
    letter-spacing: 0.4px;
  }
  .contact-list {
    position: absolute;
    left: 300px;
    top: 222px;
    list-style: none;
  }
  .contact-item {
    display: flex;
    align-items: center;
    gap: 18px;
    height: 44px;
    font-weight: 400;
    font-size: 19px;
    color: var(--text-light);
    letter-spacing: 0.4px;
  }
  .contact-icon { width: 22px; height: 22px; flex: none; }
</style>
</head>
<body>
<main class="sheet">
  <section class="card card--front">
    <div class="front-pattern" role="img" aria-label="Soft light grey hexagon texture across the card face"></div>
    <span class="brand-name">CORVALIN</span>
  </section>

  <section class="card card--back">
    <div class="title-band">
      <span class="title-band__label">Biotechnology</span>
      <span class="title-band__rule"></span>
    </div>
    <div class="side-tab"></div>
    <div class="person">
      <p class="person__name">Dana Whitlow</p>
      <p class="person__title">Genetic Consultant</p>
    </div>
    <ul class="contact-list">
      <li class="contact-item">
        <svg class="contact-icon" viewBox="0 0 24 24" aria-hidden="true">
          <path fill="var(--accent-green)" d="M6.6 10.8a15 15 0 0 0 6.6 6.6l2.2-2.2c.3-.3.7-.4 1-.2 1.1.4 2.3.6 3.6.6.6 0 1 .4 1 1V20c0 .6-.4 1-1 1A17 17 0 0 1 3 4c0-.6.4-1 1-1h3.5c.6 0 1 .4 1 1 0 1.3.2 2.5.6 3.6.1.3 0 .7-.2 1z"/>
        </svg>
        <span>01632960481</span>
      </li>
      <li class="contact-item">
        <svg class="contact-icon" viewBox="0 0 24 24" aria-hidden="true">
          <rect x="2" y="5" width="20" height="14" fill="var(--accent-green)"/>
          <path d="M2 5l10 8 10-8" fill="none" stroke="var(--card-dark)" stroke-width="1.6"/>
        </svg>
        <span>hello@corvalinbio.com</span>
      </li>
      <li class="contact-item">
        <svg class="contact-icon" viewBox="0 0 24 24" aria-hidden="true">
          <circle cx="12" cy="12" r="10" fill="var(--accent-green)"/>
          <g fill="none" stroke="var(--card-dark)" stroke-width="1.3">
            <ellipse cx="12" cy="12" rx="4.5" ry="10"/>
            <path d="M2 12h20M4 7h16M4 17h16M12 2v20"/>
          </g>
        </svg>
        <span>www.corvalinbio.com</span>
      </li>
    </ul>
  </section>
</main>
</body>
</html>
```